Healthcare technology firm needs business card layout. Logo provided.

We need a business card design for a new healthcare technology company called Kevrimo.com. The logo is already done so that will be used in the design. We assist patients and their families manage their personal health finances. Our initial product is our web site membership that includes educational content on your health benefits, tools, and downloadable forms.

We would like to see designs that use our existing logo or extend the logo in a creative way. Should be very consumer friendly.

```html
<!DOCTYPE html>
<html lang="en">
<head>
<meta charset="utf-8">
<title>Kevrimo.com Business Card</title>
<link rel="stylesheet" href="https://fonts.googleapis.com/css2?family=Questrial&family=Figtree:ital,wght@0,400;0,700;1,400&display=swap">
<style>
  :root {
    --page: #ffffff;
    --card: #ffffff;
    --card-edge: #eeeeee;
    --brand-blue: #0d3ef0;
    --ink: #111111;
    --band-green: #2cf04a;
    --band-teal: #2183a4;
    --band-mid: #1563d8;
    --band-blue: #0c3aff;
  }
  html, body {
    margin: 0;
    padding: 0;
    width: 1200px;
    height: 900px;
    overflow: hidden;
    background: var(--page);
  }
  .card {
    position: absolute;
    left: 65px;
    top: 127px;
    width: 1063px;
    height: 650px;
    background: var(--card);
    border: 1px solid var(--card-edge);
    box-sizing: border-box;
  }
  .brand {
    position: absolute;
    right: 58px;
    top: 44px;
    margin: 0;
    font-family: "Questrial", sans-serif;
    font-weight: 400;
    font-size: 98px;
    line-height: 1;
    letter-spacing: 1px;
    color: var(--brand-blue);
  }
  .tagline {
    position: absolute;
    right: 56px;
    top: 179px;
    margin: 0;
    text-align: right;
    font-family: "Figtree", sans-serif;
    font-style: italic;
    font-size: 25px;
    line-height: 29px;
    color: var(--brand-blue);
  }
  .holder {
    position: absolute;
    left: 59px;
    top: 218px;
    margin: 0;
    font-family: "Figtree", sans-serif;
    color: var(--brand-blue);
    white-space: nowrap;
  }
  .holder-name {
    font-weight: 700;
    font-size: 38px;
  }
  .holder-title {
    font-family: "Questrial", sans-serif;
    font-size: 25px;
    margin-left: 10px;
  }
  .contact {
    position: absolute;
    left: 59px;
    top: 356px;
    margin: 0;
    font-family: "Questrial", sans-serif;
    font-size: 28px;
    line-height: 42px;
    letter-spacing: 0.6px;
    color: var(--ink);
    font-style: normal;
    white-space: nowrap;
  }
  .brand-band {
    position: absolute;
    left: 0;
    top: 500px;
    width: 100%;
    height: 70px;
    background: linear-gradient(90deg, var(--band-green) 0%, var(--band-teal) 38%, var(--band-mid) 60%, var(--band-blue) 82%, var(--band-blue) 100%);
  }
</style>
</head>
<body>
  <main class="card">
    <h1 class="brand">KEVRIMO</h1>
    <p class="tagline">Simplifying your<br>health finances</p>
    <p class="holder"><span class="holder-name">Marla J. Voss</span><span class="holder-title">CEO</span></p>
    <address class="contact">
      Kansas City Fort Myers Phoenix Singapore<br>
      M: 239-555-0147<br>
      www.kevrimo.com
    </address>
    <div class="brand-band"></div>
  </main>
</body>
</html>
```